Homvuk Business Card Project showing the logo and a bellan image on the rear

Design a whacky but professional business card, the logo is for the front and the Bellan image is for the rear. Happy to consider other open source Bellan Images if the designer wants to select one from the web. Homvuk is a competitor to TKU.com.au and Parcelo.com.au and is based around every property in Australia

Target Market(s)

Business

Contact Information for Business Card

Name, Title, Email, Web, Phone Number

Font styles to use
Other font styles liked:
• avenir

Requirements
Must have
• Image on Back logo on front
Nice to have
• Happy to consider other images on rear, preftably Oskar Bellan. Image supplied I own, we can use open source other Bellan Images

```html
<!DOCTYPE html>
<html lang="en">
<head>
<meta charset="utf-8">
<title>Homvuk Business Card</title>
<link rel="stylesheet" href="https://fonts.googleapis.com/css2?family=Figtree:wght@400;600;700;800&family=Roboto:wght@400;500&display=swap">
<style>
  :root {
    --backdrop: #232323;
    --card: #ececec;
    --ink: #111111;
    --orange: #ee8a0c;
    --text: #1c1c1c;
  }
  * { box-sizing: border-box; margin: 0; padding: 0; }
  html, body { width: 1200px; height: 1138px; overflow: hidden; }
  body { background: var(--backdrop); position: relative; font-family: "Roboto", Arial, sans-serif; color: var(--text); }

  .card { position: absolute; width: 620px; height: 376px; background: var(--card); border-radius: 16px; overflow: hidden; }
  .card-front { left: 274px; top: 186px; }
  .card-back { left: 276px; top: 608px; }

  .brand { position: absolute; display: flex; align-items: center; }
  .brand-mark { background: var(--orange); display: block; }
  .brand-name { font-family: "Figtree", Arial, sans-serif; font-weight: 700; color: var(--ink); line-height: 1; }

  .card-front .brand { left: 144px; top: 52px; gap: 28px; }
  .card-front .brand-mark { width: 78px; height: 78px; }
  .card-front .brand-name { font-size: 80px; }
  .front-url { position: absolute; left: 0; right: 0; top: 140px; text-align: center; font-family: "Figtree", Arial, sans-serif; font-size: 16px; letter-spacing: 13px; padding-left: 40px; color: var(--ink); }
  .cityscape { position: absolute; left: 0; right: 0; top: 196px; bottom: 0;
    background: linear-gradient(90deg, #e8407a 0%, #3d8fd6 18%, #f08a2e 34%, #b8d64a 50%, #e8407a 66%, #5ab9e0 82%, #f2b233 100%); }

  .wave { position: absolute; left: 0; top: 0; }
  .tagline { position: absolute; right: 38px; top: 26px; text-align: right; font-size: 16px; line-height: 24px; color: var(--ink); }
  .card-back .brand { left: 30px; top: 98px; gap: 24px; }
  .card-back .brand-mark { width: 92px; height: 92px; }
  .card-back .brand-name { font-size: 88px; }

  .contacts { position: absolute; left: 30px; top: 250px; list-style: none; font-size: 16px; }
  .contacts li { display: flex; align-items: center; gap: 14px; height: 24px; }
  .contacts svg { width: 16px; height: 16px; }
  .contacts .accent { color: var(--orange); }
  .address { position: absolute; left: 30px; top: 320px; font-size: 16px; }

  .person { position: absolute; right: 34px; top: 272px; text-align: right; }
  .person-name { font-family: "Figtree", Arial, sans-serif; font-weight: 600; font-size: 25px; color: var(--orange); line-height: 1.1; }
  .person-title { font-size: 16px; margin-top: 4px; }
</style>
</head>
<body>
  <section class="card card-front">
    <div class="brand">
      <span class="brand-mark"></span>
      <span class="brand-name">Homvuk</span>
    </div>
    <p class="front-url">www.homvuk.com</p>
    <div class="cityscape" role="img" aria-label="Colourful cartoon city skyline illustration with a row of tram carriages"></div>
  </section>

  <section class="card card-back">
    <svg class="wave" width="620" height="376" viewBox="0 0 620 376" aria-hidden="true">
      <path d="M0,0 H620 V98 C560,118 470,118 390,88 C300,52 200,18 110,26 C60,30 25,40 0,50 Z" fill="var(--orange)"/>
      <path d="M0,52 C60,30 140,14 200,20 C280,28 340,62 410,96 C480,126 560,126 620,106" fill="none" stroke="var(--ink)" stroke-width="9"/>
      <path d="M40,60 C120,20 200,22 280,46" fill="none" stroke="var(--card)" stroke-width="3"/>
    </svg>
    <p class="tagline">Buying, Selling<br>and Research</p>
    <div class="brand">
      <span class="brand-mark"></span>
      <span class="brand-name">Homvuk</span>
    </div>
    <ul class="contacts">
      <li>
        <svg viewBox="0 0 16 16" aria-hidden="true"><circle cx="8" cy="8" r="6.5" fill="none" stroke="#ee8a0c" stroke-width="1.4"/><path d="M5.5,5 l1.5,0 0.6,1.6 -0.9,0.8 c0.4,0.9 1,1.5 1.9,1.9 l0.8,-0.9 1.6,0.6 0,1.5 c-3,0.2 -5.7,-2.5 -5.5,-5.5z" fill="#ee8a0c"/></svg>
        <span>(00) 4141 5757</span>
      </li>
      <li>
        <svg viewBox="0 0 16 16" aria-hidden="true"><rect x="1.5" y="3.5" width="13" height="9" fill="#ee8a0c"/><path d="M1.5,3.5 L8,9 L14.5,3.5" fill="none" stroke="#ececec" stroke-width="1.2"/></svg>
        <span>carver@homvuk.com</span>
      </li>
      <li>
        <svg viewBox="0 0 16 16" aria-hidden="true"><circle cx="8" cy="8" r="6.5" fill="#ee8a0c"/><path d="M1.5,8 H14.5 M8,1.5 V14.5 M8,1.5 C4.5,5 4.5,11 8,14.5 M8,1.5 C11.5,5 11.5,11 8,14.5" fill="none" stroke="#ececec" stroke-width="1"/></svg>
        <span>www.<span class="accent">homvuk</span>.com</span>
      </li>
    </ul>
    <p class="address">Level 4, 18 Harbour Lane, Sydney 2000, AU</p>
    <div class="person">
      <p class="person-name">Noel Carver</p>
      <p class="person-title">Founder &amp; CEO</p>
    </div>
  </section>
</body>
</html>
```